New business card with our logo

we finalized our logo with the help of pixel harbor - now we need a business card using that logo. we are a metal service center providing raw steel and metal products for fabricating, contractors, artists, etc. we have the wording for the back of the card figured out (attached, no deviations from text please), just need help putting it all together.
Contact Information for Business Card
would like the look of steel somehow incorporated in the design ... would like the black part of the logo to be steel or silver color (the S & MORROW)
Font styles to use
Other font styles liked:
- calibri, arial, similar to those, modern looking
Colors
Designer to choose colors to be used in the design.
Requirements
Must have
- Back of card must haves are attached (no deviations from wording please).
- FRONT of card:
- logo
- address
- name
- office tel
- cell
- fax
- website
- address
Nice to have
- incorporate the look of steel or element of steel somehow
- names of the staff on front not in all caps, i.e. Tereza not TEREZA
- this industry is more industrial, not coffee or flower shop so design should be aligned with that
- design should be classic and tasteful

```html
<!DOCTYPE html>
<html lang="en">
<head>
<meta charset="UTF-8">
<title>Morrow Steel Business Card</title>
<link href="https://fonts.googleapis.com/css2?family=Montserrat:wght@400;500;600;700&display=swap" rel="stylesheet">
<style>
  :root {
    --backdrop: #d9dadc;
    --card-dark: #2b2c2e;
    --card-light: #ffffff;
    --steel-blue: #0f6fbd;
    --ink: #2a2b2d;
    --text-light: #f2f2f2;
  }
  * { margin: 0; padding: 0; box-sizing: border-box; }
  html, body { width: 1200px; height: 930px; overflow: hidden; }
  body {
    background: var(--backdrop);
    font-family: "Montserrat", Arial, sans-serif;
    position: relative;
  }
  .card {
    position: absolute;
    width: 580px;
    height: 330px;
    border-radius: 16px;
    overflow: hidden;
    box-shadow: 0 10px 30px rgba(0,0,0,0.25);
  }

  /* Back side */
  .card-back {
    left: 60px; top: 70px;
    background: var(--card-dark);
    color: var(--text-light);
  }
  .card-back .brand {
    position: absolute; left: 70px; top: 62px;
    display: flex; align-items: center; gap: 16px;
  }
  .brand-dot {
    width: 58px; height: 58px; border-radius: 50%;
    border: 5px solid var(--steel-blue);
    flex: none;
  }
  .brand-name {
    font-weight: 700; font-size: 40px; letter-spacing: 1px;
    color: var(--steel-blue); white-space: nowrap;
  }
  .back-copy {
    position: absolute; left: 70px; top: 158px; width: 440px;
  }
  .service-title {
    font-weight: 600; font-size: 24px; color: var(--steel-blue); letter-spacing: 0.5px;
  }
  .service-list {
    font-weight: 400; font-size: 17px; margin-top: 2px; letter-spacing: 0.3px;
  }
  .back-rule {
    height: 2px; background: var(--steel-blue); margin: 10px 0 10px;
  }
  .product-line {
    font-weight: 600; font-size: 14.5px; line-height: 1.5;
  }
  .tagline {
    font-weight: 500; font-size: 17px; color: var(--steel-blue); margin-top: 8px;
  }

  /* Front side */
  .card-front {
    left: 560px; top: 540px;
    background: var(--card-light);
    color: var(--ink);
  }
  .card-front .brand {
    position: absolute; left: 38px; top: 62px;
    display: flex; align-items: center; gap: 10px;
  }
  .card-front .brand-dot { width: 40px; height: 40px; border-width: 4px; }
  .card-front .brand-name { font-size: 25px; letter-spacing: 0.5px; }
  .person {
    position: absolute; right: 34px; top: 34px; text-align: right;
  }
  .person-name {
    font-weight: 600; font-size: 26px; color: var(--steel-blue); line-height: 1.1;
  }
  .person-role { font-size: 14px; color: var(--ink); margin-top: 2px; }
  .front-rule {
    position: absolute; left: 190px; right: 30px; top: 112px;
    height: 2px; background: var(--steel-blue);
  }
  .address {
    position: absolute; right: 34px; top: 124px; text-align: right;
    font-size: 14px; line-height: 1.45;
  }
  .contacts {
    position: absolute; left: 40px; top: 158px;
    list-style: none; font-size: 15px; line-height: 1.4;
  }
  .contacts li { display: flex; align-items: center; gap: 10px; }
  .contacts svg { width: 12px; height: 12px; fill: var(--steel-blue); flex: none; }
  .contacts .domain { color: var(--steel-blue); }
  .wave {
    position: absolute; left: 0; bottom: 0; width: 580px; height: 150px;
  }
</style>
</head>
<body>

<section class="card card-back">
  <div class="brand">
    <span class="brand-dot"></span>
    <span class="brand-name">MORROW STEEL</span>
  </div>
  <div class="back-copy">
    <p class="service-title">METAL SERVICE CENTER</p>
    <p class="service-list">CUT - SHEAR - PUNCH - LIGHT FAB</p>
    <div class="back-rule"></div>
    <p class="product-line">Structural Steel - Stainless &amp; aluminm</p>
    <p class="product-line">Building Components - Rebar - Decking ..and more</p>
    <p class="tagline">Cut to size, Pick-up or Delivered!</p>
  </div>
</section>

<section class="card card-front">
  <div class="brand">
    <span class="brand-dot"></span>
    <span class="brand-name">MORROW STEEL</span>
  </div>
  <div class="person">
    <p class="person-name">Daniel Hayes</p>
    <p class="person-role">Director</p>
  </div>
  <div class="front-rule"></div>
  <p class="address">402 Alder Creek Rd.<br>Franklin, TN 37064</p>

  <ul class="contacts">
    <li><svg viewBox="0 0 12 12"><path d="M2 1l2 0 1 3-1.5 1a6 6 0 0 0 3.5 3.5L8 7l3 1v2c0 .6-.4 1-1 1A9 9 0 0 1 1 2c0-.6.4-1 1-1z"/></svg><span>+330 4812-3307</span></li>
    <li><svg viewBox="0 0 12 12"><path d="M3 0h6a1 1 0 0 1 1 1v10a1 1 0 0 1-1 1H3a1 1 0 0 1-1-1V1a1 1 0 0 1 1-1zm0 2v7h6V2z"/></svg><span>+330 4812-3390</span></li>
    <li><svg viewBox="0 0 12 12"><path d="M1 4h10v6H1zM3 1h6v2H3zM3 8h6v3H3z"/></svg><span>+330 4812-3315</span></li>
    <li><svg viewBox="0 0 12 12"><path d="M0 2h12v8H0zm1 1v.3l5 3.2 5-3.2V3zm0 1.5V9h10V4.5L6 7.7z"/></svg><span>info@morrowsteel.com</span></li>
    <li><svg viewBox="0 0 12 12"><circle cx="6" cy="6" r="5.5"/></svg><span>www.<span class="domain">morrowsteel</span>.com</span></li>
  </ul>

  <svg class="wave" viewBox="0 0 580 150" preserveAspectRatio="none" aria-hidden="true">
    <path d="M0 150 L0 144 C200 144 300 114 380 64 C450 24 520 14 580 12 L580 150 Z" fill="var(--steel-blue)"/>
    <path d="M0 139 C200 139 300 109 376 59 C446 19 516 9 580 7" fill="none" stroke="var(--ink)" stroke-width="5"/>
    <path d="M0 135 C200 135 300 105 374 55 C444 15 514 5 580 3" fill="none" stroke="#ffffff" stroke-width="3"/>
  </svg>
</section>

</body>
</html>
```